Mobile mechanics business card

i need a business card for my new business im a mobile mechanic who works on farm machines, ie tractors and construction machines ie bulldozers and frost protection wind machines in orchards so would like those three machines in the back ground to show the customers what i am specializing in. just go for it and suprise me!!

Target Market(s)

orchard owner, farm owners and contractors

Industry/Entity Type

Construction

Contact Information for Business Card

Rob kellaway, mobile mechanic, Ph 0274835106, Email robk.kellaway24@mailnest.example

```html
<!DOCTYPE html>
<html lang="en">
<head>
<meta charset="utf-8">
<title>Rob Kellaway – Mobile Mechanic Business Card</title>
<link rel="stylesheet" href="https://fonts.googleapis.com/css2?family=Open+Sans:ital,wght@0,400;0,700;1,400&display=swap">
<style>
  :root {
    --page-bg: #ffffff;
    --card-bg: #b6e0d9;
    --emblem-tone: #a3d3ca;
    --navy: #27497a;
    --ink-label: #2c3e5a;
    --accent-blue: #2f7fe6;
    --rule-blue: #7fb0e8;
  }

  * { margin: 0; padding: 0; box-sizing: border-box; }

  html, body {
    width: 1200px;
    height: 848px;
    overflow: hidden;
    background: var(--page-bg);
  }

  .canvas {
    position: relative;
    width: 1200px;
    height: 848px;
  }

  .business-card {
    position: absolute;
    left: 206px;
    top: 182px;
    width: 788px;
    height: 484px;
    border-radius: 36px;
    background: var(--card-bg);
    overflow: hidden;
    font-family: "Open Sans", Arial, sans-serif;
  }

  .card-emblem-area {
    position: absolute;
    left: 62px;
    top: 92px;
    width: 256px;
    height: 290px;
    border-radius: 8px;
    background: var(--emblem-tone);
  }

  .identity {
    position: absolute;
    left: 360px;
    top: 236px;
  }

  .identity__name {
    display: flex;
    align-items: center;
    gap: 10px;
    font-size: 28px;
    font-weight: 700;
    letter-spacing: 1.5px;
    line-height: 1;
    text-transform: uppercase;
    white-space: nowrap;
    color: var(--navy);
  }

  .identity__dot {
    width: 18px;
    height: 18px;
    border-radius: 50%;
    background: #ffffff;
  }

  .identity__role {
    margin-top: 8px;
    font-size: 17px;
    font-style: italic;
    color: var(--accent-blue);
    line-height: 1.1;
  }

  .identity__rule {
    margin-top: 16px;
    width: 64px;
    height: 2px;
    background: var(--rule-blue);
  }

  .contact-list {
    position: absolute;
    left: 360px;
    top: 346px;
    display: grid;
    grid-template-columns: 70px auto;
    row-gap: 4px;
    font-size: 16px;
    line-height: 1.3;
    white-space: nowrap;
  }

  .contact-list dt {
    font-style: italic;
    color: var(--ink-label);
  }

  .contact-list dd {
    font-weight: 700;
    color: var(--accent-blue);
  }
</style>
</head>
<body>
  <main class="canvas">
    <section class="business-card" aria-label="Business card for Rob Kellaway, mobile mechanic">
      <div class="card-emblem-area" role="img" aria-label="Large embossed emblem area in navy blue"></div>

      <div class="identity">
        <h1 class="identity__name">Rob Kellaway <span class="identity__dot" aria-hidden="true"></span></h1>
        <p class="identity__role">mobile mechanic</p>
        <div class="identity__rule" aria-hidden="true"></div>
      </div>

      <dl class="contact-list">
        <dt>mobile.</dt>
        <dd>02 7483 5106</dd>
        <dt>email.</dt>
        <dd>robk.kellaway24@mailnest.example</dd>
      </dl>
    </section>
  </main>
</body>
</html>
```